Crumbly Corner needs a business card

Crumbly Corner needs an attractive, playful, and exciting business card design to attract potential buyers. I have included our logo, label, and social media design files along with the fonts and colors for ideas. For the logo file, please only pay attention to the purple background with white text. I want a card with premium matte and metallic finish. I want my name included, e-mail, and phone number. The logo must be included, and then use the label design and social media design files to add creativity to the design. Only the fonts that are provided should be used as well.

Name: Gregory Halvorsen
Phone: 555-274-8106
E-mail: ghalvorsen@crumblycornerco.example

Industry/Entity Type

Business

Contact Information for Business Card

I want a card with premium matte and metallic finish. I want my name included, e-mail, and phone number. The logo must be included, and then use the label design and social media design files to add creativity to the design. Only the fonts that are provided should be used as well.

Name: Gregory Halvorsen
Phone: 555-274-8106

Colors
6b449b

Requirements
Must have
• My logo, my fonts, my colors, my designs to some degree, and my character

```html
<!DOCTYPE html>
<html lang="en">
<head>
<meta charset="utf-8">
<title>Crumbly Corner – Business Card</title>
<link rel="stylesheet" href="https://fonts.googleapis.com/css2?family=Great+Vibes&family=Lato:wght@400;900&display=swap">
<style>
  :root {
    --backdrop: #e6e3e0;
    --card-black: #0b0b0c;
    --card-edge: #1a1a1c;
    --brand-violet: #5a4fd6;
    --name-blue: #2f6fd8;
    --contact-white: #e8e8ec;
    --icon-blue: #3f63d9;
    --foil-silver: #d4d5da;
  }
  html, body {
    margin: 0;
    width: 1200px;
    height: 900px;
    overflow: hidden;
    background: var(--backdrop);
  }
  .canvas {
    width: 1200px;
    height: 900px;
    display: flex;
    align-items: center;
    justify-content: center;
    gap: 40px;
  }
  .card {
    position: relative;
    width: 540px;
    height: 309px;
    background: var(--card-black);
    border: 1px solid var(--card-edge);
    box-shadow: 0 10px 28px rgba(0,0,0,0.25);
    overflow: hidden;
  }
  .brand-lockup {
    display: flex;
    flex-direction: column;
    align-items: center;
    gap: 10px;
    font-family: "Lato", sans-serif;
    font-weight: 900;
    text-align: center;
    line-height: 1;
  }
  .brand-mark {
    border-radius: 50%;
    flex: none;
  }
  .card-front .brand-lockup {
    position: absolute;
    top: 26px;
    left: 310px;
    width: 200px;
    font-size: 40px;
    color: var(--brand-violet);
  }
  .card-front .brand-mark {
    width: 84px;
    height: 84px;
    background: var(--brand-violet);
  }
  .contact-name {
    position: absolute;
    left: 40px;
    top: 182px;
    margin: 0;
    font-family: "Great Vibes", cursive;
    font-weight: 400;
    font-size: 36px;
    line-height: 1.1;
    color: var(--name-blue);
  }
  .contact-list {
    position: absolute;
    left: 42px;
    top: 232px;
    margin: 0;
    padding: 0;
    list-style: none;
    font-family: "Lato", sans-serif;
    font-size: 15px;
    color: var(--contact-white);
  }
  .contact-list li {
    display: flex;
    align-items: center;
    gap: 8px;
    margin-bottom: 9px;
  }
  .contact-icon {
    width: 13px;
    height: 13px;
    fill: var(--icon-blue);
    flex: none;
  }
  .card-back {
    display: flex;
    align-items: center;
    justify-content: center;
  }
  .card-back .brand-lockup {
    font-size: 50px;
    color: var(--foil-silver);
  }
  .card-back .brand-mark {
    width: 104px;
    height: 104px;
    background: var(--foil-silver);
  }
</style>
</head>
<body>
<main class="canvas">
  <section class="card card-front" aria-label="Card front">
    <div class="brand-lockup">
      <span class="brand-mark"></span>
      <span class="brand-name">Crumbly<br>Corner</span>
    </div>
    <h1 class="contact-name">Gregory Halvorsen</h1>
    <ul class="contact-list">
      <li>
        <svg class="contact-icon" viewBox="0 0 16 16" aria-hidden="true">
          <path d="M3 1h3l1.5 4-2 1.3a9 9 0 0 0 4.2 4.2L11 8.5l4 1.5v3a2 2 0 0 1-2 2A12 12 0 0 1 1 3a2 2 0 0 1 2-2z"/>
        </svg>
        <span>555-274-8106</span>
      </li>
      <li>
        <svg class="contact-icon" viewBox="0 0 16 16" aria-hidden="true">
          <path d="M1 3h14v10H1z M2 4l6 5 6-5" fill="none" stroke="#3f63d9" stroke-width="1.6"/>
        </svg>
        <span>ghalvorsen@crumblycornerco.example</span>
      </li>
    </ul>
  </section>
  <section class="card card-back" aria-label="Card back">
    <div class="brand-lockup">
      <span class="brand-mark"></span>
      <span class="brand-name">Crumbly<br>Corner</span>
    </div>
  </section>
</main>
</body>
</html>
```